Flyer Design Project

Family owned and operated roof repair, cleaning and restoration business. Offering quality service and product at a quality price. Have been in existence for over 25 years.
I have just had a logo designed for the business. I would like to generate business by getting people to look at their roof and consider the maintenance and appearance.
Must generate a serious approach as there have been some operators who have acted poorly.
We DO NOT pressure sell, but gladly provide quotes and advice. We only use the best quality products and we are a licensed applicator of this product.
Our finished product will protect homes and increase their value.
Target Market(s)
Home owners who have a house with concrete roof tiles.
Industry/Entity Type
Business
Look and feel

```html
<!DOCTYPE html>
<html lang="en">
<head>
<meta charset="utf-8">
<title>Ironbark Roof Restoration – Flyer</title>
<link href="https://fonts.googleapis.com/css2?family=Roboto+Condensed:wght@700&family=PT+Sans:ital,wght@0,400;0,700;1,700&display=swap" rel="stylesheet">
<style>
  :root {
    --page-bg: #d6d9dc;
    --paper: #ffffff;
    --ink: #1a1a1a;
    --brand-blue: #2f7ba6;
    --brand-blue-dark: #1f5f86;
    --sticker-light: #6fb9e4;
    --sticker-dark: #1d6fa8;
    --black: #0b0b0b;
    --white: #ffffff;
    --photo-a: #f4efec;
    --photo-b: #d9b3aa;
    --photo-c: #c9a07a;
  }
  * { box-sizing: border-box; margin: 0; padding: 0; }
  html, body { width: 1200px; height: 900px; overflow: hidden; }
  body { background: var(--page-bg); font-family: "PT Sans", sans-serif; color: var(--ink); }

  .flyer {
    position: absolute; left: 320px; top: 50px;
    width: 560px; height: 800px;
    background: var(--paper);
    box-shadow: 0 6px 22px rgba(0,0,0,.25);
    overflow: hidden;
  }

  .hero-photo {
    position: absolute; left: 0; top: 0; width: 560px; height: 370px;
    background:
      linear-gradient(160deg, transparent 55%, var(--photo-c) 100%),
      linear-gradient(200deg, var(--photo-b) 0%, var(--photo-a) 40%, var(--photo-a) 60%, var(--photo-b) 100%);
  }

  .brand-block {
    position: absolute; left: 0; top: 0; width: 190px; height: 106px;
    background: var(--black);
    display: flex; flex-direction: column; justify-content: center; align-items: center;
  }
  .brand-name {
    font-family: "PT Sans", sans-serif; font-weight: 700;
    color: var(--white); font-size: 17px; line-height: 22px; text-align: center;
    letter-spacing: .4px; white-space: nowrap;
  }

  .headline-band { position: absolute; left: 0; top: 370px; width: 560px; height: 68px; }
  .headline-band svg { position: absolute; inset: 0; }
  .headline {
    position: relative; z-index: 1;
    font-family: "Roboto Condensed", sans-serif; font-weight: 700;
    color: var(--white); font-size: 20.5px; line-height: 27px;
    text-align: center; padding-top: 8px;
    text-shadow: 0 1px 2px rgba(0,0,0,.45);
  }

  .body-copy {
    position: absolute; left: 16px; top: 452px; width: 530px;
    font-size: 11.6px; line-height: 14.6px;
  }
  .body-copy p + p { margin-top: 11px; width: 388px; }

  .sticker { position: absolute; left: 412px; top: 555px; width: 140px; height: 140px; }
  .sticker-text {
    position: absolute; left: 0; top: 0; width: 140px; height: 140px;
    display: flex; flex-direction: column; justify-content: center; align-items: center;
    transform: rotate(-22deg);
    font-weight: 700; font-style: italic; color: var(--white);
    font-size: 15px; line-height: 17px; text-align: center;
    text-shadow: 0 1px 2px rgba(0,0,0,.4);
  }
  .sticker-text .years { font-size: 20px; line-height: 24px; }

  .contact-tab { position: absolute; left: 382px; top: 707px; width: 178px; height: 23px; }
  .contact-tab svg { position: absolute; inset: 0; }
  .contact-tab span {
    position: relative; display: block; text-align: center; padding-left: 6px;
    font-weight: 700; color: var(--white); font-size: 14px; line-height: 24px;
  }

  .contact-bar {
    position: absolute; left: 0; top: 729px; width: 560px; height: 49px;
    background: var(--brand-blue);
    display: flex; align-items: center; color: var(--white);
    font-size: 12.5px; line-height: 16px;
  }
  .contact-col { padding: 0 14px; }
  .contact-col + .contact-col { border-left: 1px solid rgba(255,255,255,.8); }
  .contact-address { width: 256px; padding-left: 16px; }
  .contact-phone { width: 134px; }
  .footer-strip { position: absolute; left: 0; top: 778px; width: 560px; height: 22px; background: var(--black); }
</style>
</head>
<body>
  <main class="flyer">
    <div class="hero-photo" role="img" aria-label="Photo of a roofer in a blue cap and overalls restoring terracotta roof tiles"></div>

    <div class="brand-block">
      <div class="brand-name">IRONBARK<br>ROOF RESTORATION</div>
    </div>

    <section class="headline-band">
      <svg width="560" height="68" viewBox="0 0 560 68" aria-hidden="true">
        <rect width="560" height="68" fill="var(--black)"/>
        <polygon points="0,68 58,0 560,0 502,68" fill="var(--brand-blue)"/>
      </svg>
      <h1 class="headline">FAMILY OWNED AND OPERATED ROOF REPAIR,<br>CLEANING AND RESTORATION BUSINESS.</h1>
    </section>

    <section class="body-copy">
      <p>Your roof is the first thing people see and the last thing most owners check. Over the years concrete tiles fade, crack and gather moss and lichen, letting water into the home and pulling down its value. We are a family owned and operated business that has been repairing, cleaning and restoring roofs for more than 25 years. We only use the best quality products and are a licensed applicator of the coatings we apply, so every finished roof is sealed, protected and built to last for many years to come.</p>
      <p>We know some operators in this industry have let home owners down. That is why we never pressure sell. We gladly inspect your roof, give honest advice and provide a clear written quote with no obligation. From replacing broken tiles and repointing ridge caps to cleaning and a full protective coating, every job is done with care by our own team. A restored roof protects your home, refreshes its look and increases its value. Look at your roof today, then give us a call.</p>
    </section>

    <div class="sticker">
      <svg width="140" height="140" viewBox="0 0 140 140" aria-hidden="true">
        <defs>
          <radialGradient id="stickerFill" cx="35%" cy="30%" r="75%">
            <stop offset="0" stop-color="var(--sticker-light)"/>
            <stop offset="1" stop-color="var(--sticker-dark)"/>
          </radialGradient>
        </defs>
        <circle cx="70" cy="70" r="67" fill="#ffffff" stroke="#b9c9d4" stroke-width="1"/>
        <circle cx="70" cy="70" r="61" fill="url(#stickerFill)"/>
      </svg>
      <div class="sticker-text">
        <span>Have been in</span>
        <span>existence</span>
        <span>for over</span>
        <span class="years">25 years.</span>
      </div>
    </div>

    <div class="contact-tab">
      <svg width="178" height="23" viewBox="0 0 178 23" aria-hidden="true">
        <polygon points="0,23 22,0 152,0 178,23" fill="var(--brand-blue)"/>
      </svg>
      <span>OUR CONTACT</span>
    </div>

    <footer class="contact-bar">
      <div class="contact-col contact-address">your address goes here, Street name,<br>State, City, Zip code</div>
      <div class="contact-col contact-phone">M : 000-000-000<br>F&nbsp; : 000-000-000</div>
      <div class="contact-col contact-web">www.webname.com<br>name@domainname.com</div>
    </footer>
    <div class="footer-strip"></div>
  </main>
</body>
</html>
```